Clinical pathology box packaging and brand design

I have a box template I wanted to design for a new medical education company. The box template(top and bottom) and the illustration to use will be included and directions as to what to write on the box. The illustration should fit on the largest surface area on the side of the box.
This is the first box in our line of products and we need to have students to look at as something they can buy and have fun while learning a very difficult subject.
Updates

Need extra days to review

Target Market(s)

Medical students is my primary market. Then Nurses, physician assistants

Requirements
Must have
• https://files.plonkriver.net/doc/7Kq2Vx9TzR4mWb8NcJ3fLs6PyD1hGu5aE0oXiY2eBt/view?mode=share

```html
<!DOCTYPE html>
<html lang="en">
<head>
<meta charset="utf-8">
<title>Diagnostic Pathology Box Dielines</title>
<link href="https://fonts.googleapis.com/css2?family=Anton&family=Oswald:wght@400;500;600&family=Quicksand:wght@500;600&display=swap" rel="stylesheet">
<style>
  :root{
    --cut:#e2323a;
    --coral:#e0684f;
    --coral-deep:#c94c3a;
    --coral-light:#ef8b6e;
    --ice:#d6e9ee;
    --ink:#3f4a4c;
    --teal:#2aa8a0;
    --white:#ffffff;
    --paper:#ffffff;
  }
  *{box-sizing:border-box;margin:0;padding:0}
  html,body{width:1200px;height:888px;overflow:hidden;background:var(--paper)}
  .canvas{position:relative;width:1200px;height:888px;font-family:"Oswald",sans-serif}
  .part{position:absolute}
  .flap{position:absolute;border:1px solid var(--cut);background:var(--white)}
  .panel{position:absolute;border:1px solid var(--cut);overflow:hidden}
  .coral{background:radial-gradient(circle at 30% 25%,var(--coral-light),var(--coral) 45%,var(--coral-deep))}
  .ice{background:var(--ice)}
  .trap{position:absolute;overflow:visible}
  .title{font-family:"Anton",sans-serif;color:var(--white);line-height:.98;letter-spacing:.2px}
  .subtitle{font-family:"Oswald",sans-serif;font-weight:500;color:var(--white);letter-spacing:.1px}
  .pill{position:absolute;border:1px solid rgba(255,255,255,.7);border-radius:12px;background:rgba(190,70,50,.55);color:var(--white);padding:2px 6px;line-height:1}
  .pill b{font-family:"Oswald",sans-serif;font-weight:600;display:block}
  .pill span{font-size:5px;display:block}
  .art{position:absolute;background:linear-gradient(160deg,#8fb4c9 0%,#5e84a8 45%,#dfe6ec 100%)}
  .brand{display:flex;flex-direction:column;align-items:center;gap:2px;font-family:"Quicksand",sans-serif;font-weight:600}
  .brand .dot{border-radius:50%;border:2px solid currentColor}
  .rot{position:absolute;transform-origin:center}
  .small{font-family:"Oswald",sans-serif;font-size:5px;line-height:1.1;text-align:center}
  .flag{background:repeating-linear-gradient(to bottom,#c8313b 0 2px,#fff 2px 4px);position:relative}
  .flag::before{content:"";position:absolute;left:0;top:0;width:45%;height:55%;background:#3a4d8f}
</style>
</head>
<body>
<div class="canvas">

  <!-- Left dieline -->
  <section class="part left-dieline">
    <div class="flap" style="left:120px;top:152px;width:210px;height:30px"></div>
    <div class="panel ice" style="left:120px;top:182px;width:210px;height:76px">
      <div class="rot" style="left:0;top:0;width:210px;height:76px;transform:rotate(180deg)">
        <div class="brand" style="position:absolute;left:12px;top:10px;color:var(--ink);flex-direction:row;gap:6px;font-size:18px">
          <span class="dot" style="width:30px;height:30px;color:var(--teal)"></span><span style="color:var(--ink)">Medora</span>
        </div>
        <div class="small" style="position:absolute;left:80px;top:46px;color:var(--ink);font-size:6px">Designed by former<br>DOD Research<br>Scientists &amp; Veterans</div>
        <div class="flag" style="position:absolute;left:156px;top:50px;width:34px;height:18px"></div>
        <div class="small" style="position:absolute;left:118px;top:4px;width:80px;color:var(--ink);font-size:4px">Diagnostic Pathology · Med, Nursing &amp; PA Students</div>
      </div>
    </div>
    <div class="panel coral front" style="left:120px;top:258px;width:210px;height:215px">
      <div class="title" style="position:absolute;left:11px;top:12px;font-size:30px">DIAGNOSTIC<br>PATHOLOGY</div>
      <div class="subtitle" style="position:absolute;left:11px;top:78px;font-size:10px">A CLINICAL CASE STUDY APPROACH</div>
      <div class="art" role="img" aria-label="Illustration of a patient in a hospital bed with a nurse and a doctor holding a tablet" style="left:0;top:100px;width:210px;height:115px;clip-path:polygon(0 40%,55% 0,100% 0,100% 100%,0 100%)"></div>
      <div class="pill" style="left:13px;top:100px"><b style="font-size:11px">260 Flashcards</b><span>Practice on virtual patients</span></div>
    </div>
    <div class="panel coral" style="left:120px;top:473px;width:210px;height:74px">
      <div class="brand" style="position:absolute;left:0;right:0;top:10px;color:var(--white);font-size:16px">
        <span class="dot" style="width:30px;height:30px"></span>Medora
      </div>
    </div>
    <div class="flap" style="left:120px;top:547px;width:210px;height:30px"></div>

    <div class="panel coral" style="left:46px;top:258px;width:74px;height:215px">
      <div class="rot" style="left:-70px;top:70px;width:215px;height:74px;transform:rotate(90deg);display:flex;flex-direction:column;justify-content:center;align-items:center">
        <div class="title" style="font-size:17px;text-align:center">DIAGNOSTIC<br>PATHOLOGY</div>
        <div class="subtitle" style="font-size:5px">A CLINICAL CASE STUDY APPROACH</div>
      </div>
    </div>
    <div class="panel coral" style="left:330px;top:258px;width:74px;height:215px">
      <div class="rot" style="left:-70px;top:70px;width:215px;height:74px;transform:rotate(-90deg);display:flex;flex-direction:column;justify-content:center;align-items:center">
        <div class="title" style="font-size:17px;text-align:center">DIAGNOSTIC<br>PATHOLOGY</div>
        <div class="subtitle" style="font-size:5px">A CLINICAL CASE STUDY APPROACH</div>
      </div>
    </div>
    <div class="flap" style="left:16px;top:258px;width:30px;height:215px"></div>
    <div class="flap" style="left:404px;top:258px;width:29px;height:215px"></div>
    <svg class="trap" style="left:40px;top:225px" width="380" height="360" viewBox="0 0 380 360" fill="none" stroke="var(--cut)" stroke-width="1">
      <polyline points="6,33 13,2 80,2 80,33"/>
      <polyline points="290,33 290,2 357,2 364,33"/>
      <polyline points="6,248 13,278 80,278 80,248"/>
      <polyline points="290,248 290,278 357,278 364,248"/>
    </svg>
  </section>

  <!-- Brand mark -->
  <div class="brand" style="position:absolute;left:437px;top:102px;width:100px;color:var(--ink);font-size:25px">
    <span class="dot" style="width:46px;height:46px;color:var(--teal);border-width:3px"></span>Medora
  </div>

  <!-- Right dieline -->
  <section class="part right-dieline">
    <div class="flap" style="left:705px;top:25px;width:216px;height:31px"></div>
    <div class="panel coral" style="left:705px;top:56px;width:216px;height:207px">
      <div class="title" style="position:absolute;left:17px;top:14px;font-size:30px">DIAGNOSTIC<br>PATHOLOGY</div>
      <div class="subtitle" style="position:absolute;left:17px;top:78px;font-size:10px">A CLINICAL CASE STUDY APPROACH</div>
      <div class="art" role="img" aria-label="Illustration of a patient in a hospital bed with a nurse and a doctor holding a tablet" style="left:0;top:100px;width:216px;height:107px;clip-path:polygon(0 40%,55% 0,100% 0,100% 100%,0 100%)"></div>
      <div class="pill" style="left:17px;top:102px"><b style="font-size:11px">260 Flashcards</b><span>Practice on virtual patients</span></div>
    </div>

    <div class="flap" style="left:468px;top:263px;width:30px;height:209px"></div>
    <div class="panel coral" style="left:498px;top:263px;width:207px;height:209px">
      <div class="brand rot" style="left:50px;top:65px;width:90px;height:80px;color:var(--white);font-size:18px;flex-direction:row;justify-content:center;transform:rotate(-90deg)">
        <span class="dot" style="width:30px;height:30px"></span>Medora
      </div>
      <div class="flag" style="position:absolute;left:178px;top:100px;width:16px;height:32px"></div>
      <div class="small rot" style="left:140px;top:162px;width:90px;color:var(--white);transform:rotate(-90deg);font-size:6px">Designed by former DOD Research<br>Scientists &amp; Veterans</div>
    </div>
    <div class="panel ice" style="left:705px;top:263px;width:216px;height:209px">
      <div class="brand" style="position:absolute;left:0;right:0;top:18px;color:var(--ink);font-size:17px">
        <span class="dot" style="width:30px;height:30px;color:var(--teal)"></span>Medora
      </div>
      <div class="title" style="position:absolute;left:0;right:0;top:84px;text-align:center;font-size:23px;color:var(--ink)">DIAGNOSTIC<br>PATHOLOGY</div>
      <div class="subtitle" style="position:absolute;left:0;right:0;top:130px;text-align:center;font-size:8px;color:var(--teal)">A CLINICAL CASE STUDY APPROACH</div>
      <div class="small" style="position:absolute;left:20px;top:178px;color:var(--ink);font-size:6px">Designed by former<br>DOD Research<br>Scientists &amp; Veterans</div>
      <div class="flag" style="position:absolute;left:92px;top:180px;width:34px;height:18px"></div>
      <div class="small" style="position:absolute;left:135px;top:192px;width:70px;color:var(--ink);font-size:3.5px">Diagnostic Pathology · Med, Nursing &amp; PA Students</div>
    </div>
    <div class="panel coral" style="left:921px;top:263px;width:207px;height:209px">
      <div class="brand rot" style="left:58px;top:60px;width:90px;height:80px;color:var(--white);font-size:18px;flex-direction:row;justify-content:center;transform:rotate(90deg)">
        <span class="dot" style="width:30px;height:30px"></span>Medora
      </div>
    </div>
    <div class="flap" style="left:1128px;top:263px;width:30px;height:209px"></div>

    <div class="panel coral" style="left:705px;top:472px;width:216px;height:206px">
      <div class="brand rot" style="left:58px;top:65px;width:100px;height:80px;color:var(--white);font-size:18px;transform:rotate(180deg)">
        <span class="dot" style="width:30px;height:30px"></span>Medora
      </div>
    </div>
    <div class="flap" style="left:705px;top:678px;width:216px;height:30px"></div>

    <svg class="trap" style="left:670px;top:55px" width="290" height="630" viewBox="0 0 290 630" fill="none" stroke="var(--cut)" stroke-width="1">
      <polyline points="35,0 4,8 4,206 35,208"/>
      <polyline points="251,0 282,8 282,206 251,208"/>
      <polyline points="35,417 4,419 4,615 35,623"/>
      <polyline points="251,417 282,419 282,615 251,623"/>
    </svg>
  </section>

</div>
</body>
</html>
```